New layout for printer ink webiste

We require fresh ,easy to navigate layout for our online shop, everything can be changed even the logo open to ideas, We are cut price printer cartridge retailer pos is price, quality and speed of delivery. Design is for magento store website www.tonbrook.ie (landing page and product page).

Target Market(s)

printer owners

Industry/Entity Type

Printer

Number of Pages Required

2 page

Requirements
Must have
• clear pricing, and what we sell.
Nice to have
• must keep quick search menu, maybe different layout
Should not have
• too much going on

```html
<!DOCTYPE html>
<html lang="en">
<head>
<meta charset="utf-8">
<title>Tonbrook – Printer Cartridges</title>
<link rel="stylesheet" href="https://fonts.googleapis.com/css2?family=Mulish:wght@400;600;700;800&display=swap">
<style>
:root{
  --blue:#00aeef;
  --red:#e3191f;
  --red-band:#e11d22;
  --ink:#222;
  --text:#555;
  --muted:#999;
  --light:#f2f2f2;
  --line:#dcdcdc;
  --footer:#3b3b3b;
  --footer-text:#cfcfcf;
}
*{box-sizing:border-box;margin:0;padding:0}
html,body{width:1200px;height:2659px;overflow:hidden}
body{font-family:"Mulish",sans-serif;color:var(--text);background:#fff;position:relative}
.abs{position:absolute}

.topbar{left:0;top:0;width:1200px;height:40px;background:#efefef;font-size:17px;color:var(--ink)}
.topbar .phone{left:106px;top:9px;display:flex;align-items:center;gap:6px}
.topbar .account{right:104px;top:0;height:40px;display:flex;align-items:center;gap:12px;font-size:14px}
.topbar .cart{background:#fff;height:40px;padding:0 12px;display:flex;align-items:center;gap:6px;color:var(--blue);border-left:1px solid var(--line);border-right:1px solid var(--line)}

.header{left:0;top:40px;width:1200px;height:103px;background:#fff}
.logo{left:134px;top:22px;display:flex;align-items:center;gap:8px;font-size:38px;font-weight:800;color:var(--red)}
.logo .dot{width:14px;height:14px;background:var(--red);border-radius:50%}
.nav{right:108px;top:40px;display:flex;gap:35px;font-size:17px;color:#666;letter-spacing:.5px}
.nav .active{color:var(--ink)}

.finder{left:0;top:143px;width:1200px;height:79px;background:var(--blue)}
.select{top:20px;height:40px;background:#3cc2f3;color:#fff;font-size:15px;display:flex;align-items:center;justify-content:space-between;padding:0 14px}
.search-btn{left:929px;top:20px;width:161px;height:40px;background:#111;color:#fff;font-size:20px;font-weight:700;display:flex;align-items:center;justify-content:center}

.hero{left:0;top:222px;width:1200px;height:478px;background:linear-gradient(180deg,#fdfdfd,#e4e4e4)}
.hero-art{left:530px;top:0;width:670px;height:478px;background:radial-gradient(ellipse at 55% 50%,#ffffff 0%,#ececec 55%,#dcdcdc 100%)}
.hero-art .swatch{position:absolute;left:210px;top:210px;width:300px;height:170px;background:linear-gradient(90deg,#3ec7ee,#ec3f8f,#f6e34a,#3a3a3a);opacity:.35;border-radius:8px}
.hero-copy{left:112px;top:128px;width:420px}
.hero-copy .kicker{font-size:33px;font-weight:700;color:var(--red);line-height:1.1}
.hero-copy h1{font-size:39px;font-weight:700;color:#333;line-height:1.2;margin-top:4px}
.hero-copy p{font-size:13px;color:#666;margin-top:14px;line-height:1.6}
.btn-shop{left:112px;top:510px;width:163px;height:39px;background:var(--red);color:#fff;font-size:15px;font-weight:700;display:flex;align-items:center;justify-content:center}
.dots{left:106px;top:591px;display:flex;gap:12px}
.dots span{width:14px;height:14px;border-radius:50%;background:#999}
.dots span:first-child{background:#fff;border:2px solid #999}

.tile{top:741px;height:206px;overflow:hidden}
.tile-why{left:106px;width:326px;background:linear-gradient(135deg,#2a2a2a,#555);color:#fff;display:flex;flex-direction:column;justify-content:center;padding:0 40px}
.tile-why h3{font-size:25px;font-weight:600;text-align:center}
.tile-why p{font-size:14px;text-align:center;line-height:1.5;margin-top:4px}
.tile-combo{left:436px;width:328px;background:#fff;border:1px solid var(--line);padding:48px 24px}
.tile-combo h3{font-size:22px;font-weight:700;color:#333;line-height:1.1}
.tile-combo h3 span{color:var(--blue);display:block;font-size:24px}
.tile-combo p{font-size:11px;color:var(--muted);width:160px;margin-top:10px;line-height:1.7}
.tile-combo .art{position:absolute;right:12px;top:22px;width:130px;height:160px;background:linear-gradient(160deg,#e8e8e8,#cfd7e0);border-radius:6px}
.tile-quality{left:767px;width:328px;background:var(--red);color:#fff;text-align:center;padding-top:28px}
.tile-quality h3{font-size:22px;font-weight:600;line-height:1.1}
.tile-quality .art{margin:18px auto 0;width:170px;height:110px;background:linear-gradient(90deg,#6fd3f0,#e86aa6,#f4e36a,#555);opacity:.8;border-radius:4px 4px 0 0}

.about{left:0;top:998px;width:1200px;height:429px;background:#f3f3f3;text-align:center}
.about h2{font-size:33px;font-weight:400;color:#333;margin-top:50px}
.about p{width:900px;margin:26px auto 0;font-size:14px;line-height:1.85;color:#666}
.about p + p{margin-top:12px}
.about-art{left:0;top:225px;width:1200px;height:204px;background:linear-gradient(90deg,#f3a0b8 0%,#f3f3f3 22%,#9fdcf0 38%,#ef8fc2 50%,#f2e57a 62%,#777 72%,#f3f3f3 80%,#6ab8e8 100%);opacity:.75}

.section-title{left:106px;top:1487px;font-size:28px;font-weight:700;color:var(--red)}
.arrows{left:1022px;top:1495px;display:flex;gap:8px}
.arrows span{width:27px;height:27px;border-radius:50%;background:#e6e6e6;display:flex;align-items:center;justify-content:center}
.product{top:1547px;width:241px;height:323px;border:1px solid var(--line);background:#fff}
.product .art{margin:22px auto 0;width:190px;height:150px;border-radius:4px}
.product h4{font-size:18px;font-weight:600;color:#333;margin:32px 0 0 24px}
.product p{font-size:10px;color:var(--muted);margin:6px 24px 0;line-height:1.6}
.product .bar{position:absolute;left:0;bottom:0;width:100%;height:38px;display:flex}
.product .price{flex:1;background:#eee;display:flex;align-items:center;justify-content:center;font-size:18px;color:#333}
.product .add{flex:1;background:var(--blue);display:flex;align-items:center;justify-content:center}

.brands-title{left:0;top:1955px;width:1200px;text-align:center;font-size:30px;color:#555;letter-spacing:1px}
.brands{left:94px;top:2017px;width:994px;height:90px;display:flex;border:1px solid var(--line)}
.brands div{flex:1;border-right:1px solid var(--line);display:flex;align-items:center;justify-content:center;font-size:28px;font-weight:700;color:#9a9a9a}
.brands div:last-child{border-right:0}

.perks{left:0;top:2187px;width:1200px;height:108px;background:var(--red-band);display:flex;justify-content:center}
.perk{width:248px;display:flex;align-items:center;gap:14px;padding-left:34px;color:#fff;font-size:21px;line-height:1.1;border-right:1px solid #c8141a}
.perk:last-child{border-right:0}
.perk svg{flex:none}

.footer{left:0;top:2295px;width:1200px;height:364px;background:var(--footer);color:var(--footer-text)}
.col{top:50px}
.col h5{font-size:18px;font-weight:600;color:#fff;letter-spacing:.5px;margin-bottom:14px}
.col li{list-style:none;font-size:16px;line-height:25px}
.social{display:flex;gap:8px}
.social span{width:31px;height:31px;border:2px solid #fff;border-radius:50%}
.footer .rule{left:106px;top:275px;width:990px;height:1px;background:#555}
.copy{left:113px;top:305px;font-size:13px}
.cards{right:96px;top:300px;display:flex;gap:8px}
.cards span{width:40px;height:24px;background:#eee;border-radius:2px;font-size:8px;font-weight:700;color:#555;display:flex;align-items:center;justify-content:center}
</style>
</head>
<body>

<div class="abs topbar">
  <div class="abs phone">
    <svg width="16" height="16" viewBox="0 0 24 24"><path d="M6.6 10.8a15 15 0 0 0 6.6 6.6l2.2-2.2c.3-.3.7-.4 1-.2 1.1.4 2.3.6 3.6.6.6 0 1 .4 1 1V20c0 .6-.4 1-1 1A17 17 0 0 1 3 4c0-.6.4-1 1-1h3.5c.6 0 1 .4 1 1 0 1.3.2 2.5.6 3.6.1.3 0 .7-.2 1z" fill="#333"/></svg>
    1800 555 010
  </div>
  <div class="abs account">
    <span>REGISTER</span><span>|</span><span>LOGIN</span>
    <span class="cart"><svg width="20" height="18" viewBox="0 0 24 20"><path d="M2 7h20l-3 11H5z" fill="none" stroke="#00aeef" stroke-width="2"/><path d="M7 7l4-5M17 7l-4-5" stroke="#00aeef" stroke-width="2"/></svg>MY CART</span>
  </div>
</div>

<header class="abs header">
  <div class="abs logo">tonbrook.ie</div>
  <nav class="abs nav">
    <span class="active">HOME</span><span>ABOUT US</span><span>INKJET</span><span>LASER</span><span>PAPER</span><span>SHOP NOW</span>
  </nav>
</header>

<div class="abs finder">
  <div class="abs select" style="left:124px;width:245px">Choose Brand <svg width="14" height="9" viewBox="0 0 14 9"><path d="M1 1l6 6 6-6" stroke="#fff" stroke-width="2" fill="none"/></svg></div>
  <div class="abs select" style="left:383px;width:280px;font-size:13px">Choose Series or Cartridges <svg width="14" height="9" viewBox="0 0 14 9"><path d="M1 1l6 6 6-6" stroke="#fff" stroke-width="2" fill="none"/></svg></div>
  <div class="abs select" style="left:675px;width:240px;font-size:13px">Select Cartridge <svg width="14" height="9" viewBox="0 0 14 9"><path d="M1 1l6 6 6-6" stroke="#fff" stroke-width="2" fill="none"/></svg></div>
  <div class="abs search-btn">Search</div>
</div>

<section class="abs hero">
  <div class="abs hero-art" role="img" aria-label="Four ink cartridges with a ribbon of colour pixels flowing out"><div class="swatch"></div></div>
  <div class="abs hero-copy">
    <div class="kicker">CLASS APTENT TACITI</div>
    <h1>PRINTER CARTRIDGE</h1>
    <p>Class aptent taciti sociosqu ad litora torquent per conubia nostra per inceptos hymenaeos</p>
  </div>
</section>
<div class="abs btn-shop">SHOP NOW!</div>
<div class="abs dots"><span></span><span></span><span></span><span></span></div>

<div class="abs tile tile-why" role="img" aria-label="Office printer in use, darkened behind text">
  <h3>Why Choose Us ?</h3>
  <p>Class aptent taciti sociosqu ad litora torquent per conubia nostra per</p>
</div>
<div class="abs tile tile-combo">
  <h3>Build Your Own <span>COMBO</span></h3>
  <p>Class aptent taciti sociosqu ad litora torquent per conubia nostra per inceptos</p>
  <div class="art" role="img" aria-label="Refill ink bottles with colour squares"></div>
</div>
<div class="abs tile tile-quality">
  <h3>Top Quality Cartridges<br>100% Guarantee</h3>
  <div class="art" role="img" aria-label="Row of colour ink cartridges"></div>
</div>

<section class="abs about">
  <h2>Inkjet Cartridges</h2>
  <p>We only sell compatible and remanufactured printer ink cartridges and are fanatics when it comes to quality, scouring the world for the very best inks available at the very best prices.</p>
  <p>We know you'll find our website easy to use. We are Ireland's oldest and best supplier of inkjet cartridges for Inkjet printers. We offer Free Shipping on orders over £20 to any destination in Ireland and the UK and the rest of Europe.</p>
  <div class="abs about-art" role="img" aria-label="Cyan, magenta, yellow and black cartridges between flowing colour waves"></div>
</section>

<div class="abs section-title">LATEST PRODUCT</div>
<div class="abs arrows">
  <span><svg width="8" height="12" viewBox="0 0 8 12"><path d="M6 1L1 6l5 5" stroke="#555" stroke-width="2" fill="none"/></svg></span>
  <span><svg width="8" height="12" viewBox="0 0 8 12"><path d="M2 1l5 5-5 5" stroke="#555" stroke-width="2" fill="none"/></svg></span>
</div>

<div class="abs product" style="left:106px">
  <div class="art" role="img" aria-label="Black toner cartridge" style="background:linear-gradient(180deg,#fff 30%,#4a4a4a 45%,#222 60%,#fff 75%)"></div>
  <h4>Product Name</h4><p>Class aptent taciti sociosqu ad litora torquent per conubia nostra</p>
  <div class="bar"><span class="price">$25.99</span><span class="add"><svg width="22" height="18" viewBox="0 0 24 20"><path d="M2 7h20l-3 11H5z" fill="none" stroke="#fff" stroke-width="2"/><path d="M7 7l4-5M17 7l-4-5" stroke="#fff" stroke-width="2"/></svg></span></div>
</div>
<div class="abs product" style="left:356px">
  <div class="art" role="img" aria-label="Set of four ink cartridges" style="background:linear-gradient(90deg,#fff 10%,#7fd4ef 25%,#ec8cc0 42%,#f3e67d 60%,#444 78%,#fff 92%)"></div>
  <h4>Product Name</h4><p>Class aptent taciti sociosqu ad litora torquent per conubia nostra</p>
  <div class="bar"><span class="price">$25.99</span><span class="add"><svg width="22" height="18" viewBox="0 0 24 20"><path d="M2 7h20l-3 11H5z" fill="none" stroke="#fff" stroke-width="2"/><path d="M7 7l4-5M17 7l-4-5" stroke="#fff" stroke-width="2"/></svg></span></div>
</div>
<div class="abs product" style="left:606px">
  <div class="art" role="img" aria-label="Black laser toner unit" style="background:radial-gradient(ellipse at 50% 45%,#333 0%,#222 40%,#fff 70%)"></div>
  <h4>Product Name</h4><p>Class aptent taciti sociosqu ad litora torquent per conubia nostra</p>
  <div class="bar"><span class="price">$25.99</span><span class="add"><svg width="22" height="18" viewBox="0 0 24 20"><path d="M2 7h20l-3 11H5z" fill="none" stroke="#fff" stroke-width="2"/><path d="M7 7l4-5M17 7l-4-5" stroke="#fff" stroke-width="2"/></svg></span></div>
</div>
<div class="abs product" style="left:856px">
  <div class="art" role="img" aria-label="Five slim ink cartridges fanned out" style="background:linear-gradient(90deg,#fff 5%,#333 20%,#e54b3c 35%,#f1b73b 50%,#4bb6e6 65%,#999 80%,#fff 95%)"></div>
  <h4>Product Name</h4><p>Class aptent taciti sociosqu ad litora torquent per conubia nostra</p>
  <div class="bar"><span class="price">$25.99</span><span class="add"><svg width="22" height="18" viewBox="0 0 24 20"><path d="M2 7h20l-3 11H5z" fill="none" stroke="#fff" stroke-width="2"/><path d="M7 7l4-5M17 7l-4-5" stroke="#fff" stroke-width="2"/></svg></span></div>
</div>

<div class="abs brands-title">OUR BRANDS</div>
<div class="abs brands">
  <div>Norvell</div><div>Kestra</div><div>Dorran</div><div>Halden</div><div>Ostrel</div><div>Marrow</div>
</div>

<div class="abs perks">
  <div class="perk"><svg width="42" height="32" viewBox="0 0 42 32"><rect x="2" y="6" width="24" height="18" fill="#9e1016"/><path d="M26 12h8l6 7v5H26z" fill="#9e1016"/><circle cx="10" cy="26" r="4" fill="#9e1016"/><circle cx="33" cy="26" r="4" fill="#9e1016"/></svg><span>FREE SHIPPING<br>OVER $30</span></div>
  <div class="perk"><svg width="40" height="34" viewBox="0 0 40 34"><path d="M4 4h24v16H14l-6 6v-6H4z" fill="none" stroke="#9e1016" stroke-width="3"/><path d="M30 12h6v14h-4v5l-5-5H16" fill="none" stroke="#9e1016" stroke-width="3"/></svg><span>24/7 TELEPHONE<br>SUPPORT</span></div>
  <div class="perk"><svg width="40" height="30" viewBox="0 0 40 30"><rect x="2" y="4" width="36" height="22" rx="3" fill="#9e1016"/><rect x="2" y="9" width="36" height="4" fill="#c8141a"/></svg><span>100% SECURE<br>PAYMENT</span></div>
  <div class="perk"><svg width="40" height="40" viewBox="0 0 40 40"><circle cx="20" cy="16" r="12" fill="none" stroke="#9e1016" stroke-width="4"/><path d="M12 26l-4 12 6-3 4 5 2-10M28 26l4 12-6-3-4 5-2-10" fill="#9e1016"/></svg><span>TOP &amp; BEST<br>CARTRIDGE</span></div>
</div>

<footer class="abs footer">
  <div class="abs col" style="left:113px"><h5>COMPANY</h5><ul><li>About us</li><li>Contact Us</li><li>Help</li><li>FAQ</li><li>Privacy Policy</li></ul></div>
  <div class="abs col" style="left:316px"><h5>WHERE TO BUY</h5><ul><li>Online Shop</li><li>Become a Distributor</li></ul></div>
  <div class="abs col" style="left:560px"><h5>MY ACCOUNT</h5><ul><li>Recycle</li><li>Shipping &amp; Returns</li><li>Ordering Info</li><li>Cookies</li><li>My Account</li></ul></div>
  <div class="abs col" style="left:769px"><h5>RESOURCES</h5><ul><li>News</li><li>Blogs</li><li>Testimonials</li><li>Contact Us</li></ul></div>
  <div class="abs col" style="left:957px"><h5>FOLLOW US</h5><div class="social"><span></span><span></span><span></span><span></span></div></div>
  <div class="abs rule"></div>
  <div class="abs copy">© 2017 Company Name &nbsp;All right reserved &nbsp;Term of Use</div>
  <div class="abs cards"><span>CARDA</span><span>PAYNE</span><span>DISKO</span><span>MERIT</span><span>WALLO</span></div>
</footer>

</body>
</html>
```